Criação de Kit com 5 Layouts de Post para Redes Sociais (Facebook, Instagram e etc) para Construção & Engenharia
A empresa queria:
" Trabalho com a elaboração de projetos de engenharia em geral, sendo o maior foco e experiência os proj. de Prevenção e combate a incêndio, mas tbm na elaboração de projetos arquitetônico, estrutural, e de interiores. Regularização de obras junto a Prefeitura, Corpo de Bombeiros, Junta Ouromar, Vigilância Sanitária. Acompanhamento de Obras. "

```html
<!DOCTYPE html>
<html lang="pt-BR">
<head>
<meta charset="UTF-8">
<title>Evite despesas desnecessárias — Clara Veloni</title>
<link href="https://fonts.googleapis.com/css2?family=Archivo+Black&family=Montserrat:wght@400;500;600&display=swap" rel="stylesheet">
<style>
  :root{
    --green-deep:#1d2b27;
    --green-mid:#2c3c36;
    --gold-dark:#b8955a;
    --gold:#d6bb83;
    --gold-light:#efdfb6;
    --ink:#343a39;
    --cream:#f3efe8;
    --white:#ffffff;
  }
  *{margin:0;padding:0;box-sizing:border-box}
  html,body{width:1200px;height:1200px;overflow:hidden;background:#fff}
  .post{position:relative;width:1200px;height:1200px;overflow:hidden;font-family:"Montserrat",sans-serif;color:var(--ink)}
  .backdrop-photo{position:absolute;inset:0;background:linear-gradient(100deg,#f6f6f4 0%,#eceae6 45%,#d9d7d2 75%,#c9c6c0 100%)}
  .top-band{position:absolute;left:0;top:0;width:1200px;height:90px}
  .portrait-photo{position:absolute;left:690px;top:60px;width:440px;height:1140px;
    background:linear-gradient(180deg,#8a7a70 0%,#5a534f 22%,#2e3432 45%,#252b29 100%);
    border-radius:220px 220px 0 0;opacity:.92}
  .headline{position:absolute;left:92px;top:112px;font-family:"Archivo Black",sans-serif;font-size:55px;line-height:1.12;color:var(--green-mid);letter-spacing:0.5px;z-index:2}
  .gold-bar{position:absolute;left:0;height:26px;background:linear-gradient(90deg,var(--gold-dark),var(--gold-light) 55%,var(--gold));clip-path:polygon(0 0,100% 0,calc(100% - 18px) 100%,0 100%)}
  .gold-bar.one{top:300px;width:650px}
  .gold-bar.two{top:552px;width:520px}
  .point{position:absolute;left:96px;font-size:38px;line-height:1.28;font-weight:500;color:var(--ink)}
  .point.one{top:370px}
  .point.two{top:618px}
  .hatch{position:absolute;left:96px;top:500px;width:200px;height:20px;background:repeating-linear-gradient(115deg,var(--gold) 0 3px,transparent 3px 9px)}
  .divider{position:absolute;left:96px;top:800px;width:580px;height:80px}
  .brand-panel{position:absolute;left:0;top:900px;width:540px;height:300px}
  .brand{position:absolute;left:40px;top:1020px;width:460px;text-align:center;color:var(--white)}
  .brand-mark{display:inline-block;width:26px;height:26px;border:2px solid var(--gold);margin-bottom:22px}
  .brand-name{font-size:40px;font-weight:500;letter-spacing:4px}
  .brand-tag{margin-top:8px;font-size:15px;letter-spacing:1.5px;color:var(--gold)}
  .contact-panel{position:absolute;left:700px;top:1040px;width:500px;height:160px}
  .contact{position:absolute;left:755px;top:1064px;color:var(--ink)}
  .contact-title{font-size:21px;font-weight:500;letter-spacing:1px;margin-bottom:12px}
  .contact-line{display:flex;align-items:center;gap:12px;font-weight:600}
  .contact-line.phone{font-size:28px;margin-bottom:8px}
  .contact-line.mail{font-size:21px}
  .contact-line svg{flex:none}
</style>
</head>
<body>
<div class="post">
  <div class="backdrop-photo" role="img" aria-label="Fachada clara de uma casa residencial ao fundo, desfocada"></div>

  <svg class="top-band" viewBox="0 0 1200 90" aria-hidden="true">
    <polygon points="360,0 1200,0 1200,40 330,40" fill="var(--green-deep)"/>
    <polygon points="330,40 1200,40 1200,52 322,52" fill="var(--gold)"/>
  </svg>

  <div class="portrait-photo" role="img" aria-label="Retrato de profissional de blazer escuro, sorrindo com a mão no queixo"></div>

  <h1 class="headline">EVITE DESPESAS<br>DESNECESSÁRIAS</h1>

  <div class="gold-bar one"></div>
  <p class="point one">Contrate proficionais<br>experientes.</p>
  <div class="hatch"></div>

  <div class="gold-bar two"></div>
  <p class="point two">Projetos elaborados com<br>qualidade e a segurança<br>necessária.</p>

  <svg class="divider" viewBox="0 0 580 80" aria-hidden="true">
    <line x1="0" y1="46" x2="560" y2="46" stroke="var(--gold)" stroke-width="3"/>
    <polygon points="420,22 444,46 420,70 396,46" fill="var(--gold-light)" stroke="var(--gold)" stroke-width="2"/>
    <polygon points="497,34 509,46 497,58 485,46" fill="var(--gold)"/>
  </svg>

  <svg class="brand-panel" viewBox="0 0 540 300" aria-hidden="true">
    <polygon points="0,0 510,0 540,30 540,300 0,300" fill="var(--green-deep)"/>
    <polyline points="0,10 505,10 530,35 530,300" fill="none" stroke="var(--gold)" stroke-width="4"/>
  </svg>
  <div class="brand">
    <span class="brand-mark"></span>
    <div class="brand-name">CLARA VELONI</div>
    <div class="brand-tag">PROJETANDO COM QUALIDADE E SEGURANÇA</div>
  </div>

  <svg class="contact-panel" viewBox="0 0 500 160" aria-hidden="true">
    <polygon points="0,0 500,0 500,160 0,160" fill="var(--cream)"/>
    <polygon points="380,0 500,0 500,10 372,10" fill="var(--gold)"/>
    <polygon points="455,60 475,80 455,100 435,80" fill="var(--gold)"/>
    <polygon points="420,70 430,80 420,90 410,80" fill="var(--gold-light)"/>
  </svg>
  <div class="contact">
    <div class="contact-title">ENTRE EM CONTATO</div>
    <div class="contact-line phone">
      <svg width="28" height="28" viewBox="0 0 24 24" aria-hidden="true"><path d="M6.6 10.8a15 15 0 0 0 6.6 6.6l2.2-2.2a1 1 0 0 1 1-.25 11.4 11.4 0 0 0 3.6.57 1 1 0 0 1 1 1V20a1 1 0 0 1-1 1A17 17 0 0 1 3 4a1 1 0 0 1 1-1h3.5a1 1 0 0 1 1 1c0 1.250.2 2.460.57 3.6a1 1 0 0 1-.25 1z" fill="var(--ink)"/></svg>
      <span>(31) 98765 4321</span>
    </div>
    <div class="contact-line mail">
      <svg width="26" height="20" viewBox="0 0 26 20" aria-hidden="true"><rect x="1" y="1" width="24" height="18" rx="2" fill="none" stroke="var(--ink)" stroke-width="2"/><polyline points="2,3 13,11 24,3" fill="none" stroke="var(--ink)" stroke-width="2"/></svg>
      <span>claraveloni@mail.com</span>
    </div>
  </div>
</div>
</body>
</html>
```